Delcourt Realty Business Cards

Design business card

Target Market(s)

High-End Buyer of Real Estate over $1 million dollars

Industry/Entity Type

Realtor

Contact Information for Business Card

Lena Delcourt R(S) LIC.# 41972
Cell 555 246-1938
Email Lena@Delcourt.example
Website IsleFreshHomes.example

Also Need Cards for:

Hank Delcourt R(B) LIC# 69418
C 555 613-7052
E Hank@Delcourt.example
W IsleFreshHomes.example

Colors

Designer to choose colors to be used in the design.

Requirements
Must have
• Address on back:
• 287 Pohaku Cir. , Wailea HI 96753
• Logo on back
Nice to have
• I would like the phone numbers and email address to be big so people can read it easily
Should not have
• Very small print Except For: address (287 Pohaku Cir. Wailea HI 96753)

```html
<!DOCTYPE html>
<html lang="en">
<head>
<meta charset="utf-8">
<title>Delcourt Realty Business Cards</title>
<link href="https://fonts.googleapis.com/css2?family=Lato:wght@300;700;900&family=Source+Sans+3:wght@400;500&display=swap" rel="stylesheet">
<style>
  :root{
    --stage:#08090c;
    --red:#d50603;
    --red-light:#dc1a17;
    --red-dark:#6e0000;
    --pink:#ff3e5a;
    --white:#ffffff;
    --ink:#1b1b1b;
    --teal:#23a883;
    --rule:#9a9a9a;
  }
  *{margin:0;padding:0;box-sizing:border-box}
  html,body{width:1200px;height:1200px;overflow:hidden;background:var(--stage)}
  .card{position:absolute;left:219px;width:763px;overflow:hidden}
  .card-front{top:82px;height:493px;background:var(--red)}
  .card-back{top:615px;height:503px;background:var(--red)}
  .card svg.bg{position:absolute;inset:0;width:100%;height:100%}

  .brand-stack{position:absolute;left:70px;top:165px;width:123px;
    font-family:"Lato",sans-serif;font-weight:900;color:var(--white);
    font-size:19px;line-height:1.3;letter-spacing:2px;text-align:center}

  .agent-name{position:absolute;left:440px;top:126px;
    font-family:"Lato",sans-serif;font-size:24px;color:var(--teal);white-space:nowrap}
  .agent-name strong{font-weight:900;letter-spacing:1px}
  .agent-name .licence{font-weight:300}

  .contact-list{position:absolute;left:466px;top:308px;list-style:none;
    font-family:"Source Sans 3",sans-serif;font-size:18px;color:var(--ink)}
  .contact-list li{display:flex;align-items:center;height:33px;white-space:nowrap}
  .contact-list svg{width:16px;height:16px;margin-right:9px;flex:none}

  .rule{position:absolute;left:71px;right:59px;top:426px;border-top:1px solid var(--rule)}
  .email{position:absolute;left:0;width:763px;top:433px;text-align:center;
    font-family:"Source Sans 3",sans-serif;font-size:34px;color:var(--ink)}

  .brand-band{position:absolute;left:185px;top:227px;width:397px;height:92px;
    background:var(--white);border-radius:10px 0 0 10px}
  .brand-mark{position:absolute;left:22px;top:16px;width:60px;height:60px;background:var(--red)}
  .brand-divider{position:absolute;left:96px;top:0;width:4px;height:92px;background:var(--red)}
  .brand-name{position:absolute;left:112px;top:16px;width:148px;
    font-family:"Lato",sans-serif;font-weight:900;color:var(--red);
    font-size:23px;line-height:1.3;letter-spacing:1.5px;white-space:nowrap}
  .brand-photo{position:absolute;right:0;top:0;width:132px;height:92px;
    background:linear-gradient(90deg,#f2ece6,#c9a58a 40%,#2a2a2a)}
</style>
</head>
<body>

<section class="card card-front">
  <svg class="bg" viewBox="0 0 763 493" preserveAspectRatio="none" aria-hidden="true">
    <path d="M0,301 C40,352 120,352 250,326 C420,288 560,212 763,242 L763,265 C560,236 420,300 250,336 C120,362 40,362 0,301Z" fill="var(--pink)"/>
    <path d="M0,301 C40,362 120,362 250,336 C420,300 560,236 763,265 L763,493 L0,493Z" fill="var(--white)"/>
  </svg>

  <div class="brand-stack">DELCOURT<br>REALTY</div>

  <p class="agent-name"><strong>Lena Delcourt</strong> <span class="licence">R(S) LIC</span></p>

  <ul class="contact-list">
    <li><svg viewBox="0 0 16 16"><path d="M8 1a5 5 0 0 0-5 5c0 4 5 9 5 9s5-5 5-9a5 5 0 0 0-5-5zm0 7a2 2 0 1 1 0-4 2 2 0 0 1 0 4z" fill="var(--red)"/></svg>287 Pohaku Cir. Wailea HI 96753</li>
    <li><svg viewBox="0 0 16 16"><path d="M13 10l-2.5-1.5-1.5 1.5C7.5 9.3 6.7 8.5 6 7l1.5-1.5L6 3 3.5 3.5C3.5 9 7 12.5 12.5 12.5z" fill="var(--red)"/></svg>555 246-1938</li>
    <li><svg viewBox="0 0 16 16" fill="none" stroke="var(--red)" stroke-width="1.2"><circle cx="8" cy="8" r="6.5"/><ellipse cx="8" cy="8" rx="3" ry="6.5"/><path d="M1.5 8h13M2.5 5h11M2.5 11h11"/></svg>IsleFreshHomes.example</li>
  </ul>

  <div class="rule"></div>
  <p class="email">Lena@Delcourt.example</p>
</section>

<section class="card card-back">
  <svg class="bg" viewBox="0 0 763 503" preserveAspectRatio="none" aria-hidden="true">
    <path d="M359,0 L763,0 L763,503 L443,503 C420,330 400,120 359,0Z" fill="var(--red-light)"/>
    <path d="M0,0 C60,60 80,140 73,240 C60,330 20,400 40,503 L0,503Z" fill="var(--pink)"/>
    <path d="M0,0 C50,90 55,150 50,240 C45,330 10,400 40,503 L0,503Z" fill="var(--red-dark)"/>
    <path d="M763,0 C703,60 683,140 690,240 C703,330 743,400 723,503 L763,503Z" fill="var(--pink)"/>
    <path d="M763,0 C713,90 708,150 713,240 C718,330 753,400 723,503 L763,503Z" fill="var(--red-dark)"/>
  </svg>

  <div class="brand-band">
    <div class="brand-mark"></div>
    <div class="brand-divider"></div>
    <div class="brand-name">DELCOURT<br>REALTY</div>
    <div class="brand-photo" role="img" aria-label="Photo of the two agents"></div>
  </div>
</section>

</body>
</html>
```